Copper Lantern Bend, Wine bottle label for a cabernet

Label design for a local winery (red wine). The wine is a cabernet. Winery is located in Bryson City North Carolina where the "copper lantern bend" is located. Copper Lantern Bend is a road project started after WWII that was never finished. It ends at the end of a tunnel which then extends into the Tallow Creek Basin national park. It should label as a Cabernet and the year 2016, also include the winery logo below

Target Market(s)

Tourism market

Logo Text

Copper Lantern Bend

Requirements
Must have
• Pic of tunnel to copper lantern bend, can be simple..

```html
<!DOCTYPE html>
<html lang="en">
<head>
<meta charset="utf-8">
<title>Ridgefold Hollow Winery – Cabernet 2016</title>
<link href="https://fonts.googleapis.com/css2?family=Parisienne&family=Oswald:wght@300&family=Raleway:wght@300;400&display=swap" rel="stylesheet">
<style>
  :root {
    --paper: #ffffff;
    --ink: #111111;
    --ink-soft: #4a4a4a;
  }
  * { margin: 0; padding: 0; box-sizing: border-box; }
  html, body {
    width: 1200px;
    height: 900px;
    overflow: hidden;
    background: var(--paper);
  }
  .label {
    position: relative;
    width: 1200px;
    height: 900px;
    background: var(--paper);
    color: var(--ink);
  }
  .tunnel-art {
    position: absolute;
    left: 470px;
    top: 140px;
    width: 250px;
    height: 264px;
    border-radius: 125px 125px 0 0;
    background: linear-gradient(180deg, var(--ink) 0%, var(--ink-soft) 100%);
  }
  .winery-name {
    position: absolute;
    left: 0;
    top: 0;
    width: 1200px;
    height: 900px;
    font-weight: normal;
    color: var(--ink);
  }
  .winery-name .name-script {
    position: absolute;
    left: 0;
    width: 1156px;
    top: 408px;
    text-align: center;
    font-family: "Parisienne", cursive;
    font-size: 150px;
    line-height: 1;
  }
  .winery-name .name-sub {
    position: absolute;
    left: 0;
    width: 1182px;
    top: 554px;
    text-align: center;
    font-family: "Raleway", sans-serif;
    font-weight: 300;
    font-size: 32px;
    letter-spacing: 4px;
    line-height: 1;
  }
  .varietal {
    position: absolute;
    left: 0;
    width: 1230px;
    top: 622px;
    text-align: center;
    font-family: "Oswald", sans-serif;
    font-weight: 300;
    font-size: 52px;
    letter-spacing: 2px;
    line-height: 1.2;
    color: var(--ink);
  }
  .vintage {
    position: absolute;
    left: 0;
    width: 1218px;
    top: 700px;
    display: flex;
    justify-content: center;
    align-items: center;
    gap: 10px;
    font-family: "Raleway", sans-serif;
    font-weight: 400;
    font-size: 24px;
    color: var(--ink);
  }
  .vintage .dot {
    width: 9px;
    height: 9px;
    border-radius: 50%;
    background: var(--ink);
  }
</style>
</head>
<body>
  <main class="label">
    <div class="tunnel-art" role="img" aria-label="Illustration of a road running into a tunnel beneath mountain peaks"></div>

    <h1 class="winery-name">
      <span class="name-script">Ridgefold</span>
      <span class="name-sub">HOLLOW WINERY</span>
    </h1>

    <p class="varietal">CABERNET</p>

    <p class="vintage">
      <span class="dot"></span>
      <span class="year">2016</span>
      <span class="dot"></span>
    </p>
  </main>
</body>
</html>
```